Online Marketing Agency Website

We are an online marketing agency that specializes in search marketing (SEM) for businesses of all sizes. Our core services include local search marketing, seo, paid search, paid social, graphic design, video production/editing and website design. We have an existing website that we launched a number of years ago but it's very outdated and we're currently too busy to design a new version.

Target Market(s)

Any business that needs online marketing services with an emphasis on search marketing.

Industry/Entity Type

Ad Agency

Number of Pages Required

4 page

Font styles to use
Sans Serif

Requirements
Must have
• Home page, interior page, blog page, contact us page.
Look and feel should be modern and clean and easy to navigate.
Sections for call outs for specific services: Business Marketing Strategy, Content Creation and Marketing, Graphic & Publication Design, Pay Per Click (PPC) Management, Search Engine Optimization, Social Media Management, Video Production & Editing, Website Hosting & Management, Website Design & Development
Use color from logo that was uploaded.

```html
<!DOCTYPE html>
<html lang="en">
<head>
<meta charset="utf-8">
<title>Brightpath Digital – Online Marketing Agency</title>
<link href="https://fonts.googleapis.com/css2?family=Roboto:wght@300;400;500;700&display=swap" rel="stylesheet">
<style>
:root{
  --orange:#ff5019;
  --orange-soft:#f47a4c;
  --ink:#2e2e2e;
  --text:#555;
  --muted:#7a7a7a;
  --grey-bg:#f1f1f1;
  --sky:#d6e8fb;
  --black:#111;
  --footer:#262626;
  --photo:#c9c9c9;
  --white:#fff;
}
*{margin:0;padding:0;box-sizing:border-box}
html,body{width:1200px;height:3733px;overflow:hidden}
body{position:relative;background:var(--white);font-family:'Roboto',sans-serif;color:var(--ink)}
.abs{position:absolute}
.orange{color:var(--orange)}
.btn{position:absolute;display:flex;align-items:center;justify-content:center;background:var(--ink);color:var(--white);font-size:13px;font-weight:700;border-radius:20px;box-shadow:0 4px 6px rgba(0,0,0,.25);letter-spacing:.3px}

/* header */
.brand{left:93px;top:20px;text-align:left}
.brand-dot{width:22px;height:22px;border-radius:50%;background:var(--orange);margin:0 0 8px 50px}
.brand-name{font-size:16px;font-weight:700;color:var(--ink);letter-spacing:.3px}
.brand-tag{font-size:10px;color:var(--ink)}
.nav{top:62px;left:338px;display:flex;font-size:12px;color:var(--ink)}
.nav a{position:absolute;white-space:nowrap;text-decoration:none;color:var(--ink)}
.nav a.active{color:var(--orange)}

/* hero */
.hero-title{left:94px;top:172px;line-height:1}
.hero-title .l1{font-size:40px;font-weight:400}
.hero-title .l2{font-size:58px;font-weight:500;margin-top:8px}
.hero-title .l3{font-size:58px;font-weight:700;color:var(--orange);margin-top:4px}
.hero-lead{left:94px;top:352px;width:400px;font-size:13px;line-height:19px;color:var(--text)}
.hero-call{left:219px;top:407px;font-size:13px;line-height:18px}
.social-dot{width:24px;height:24px;border-radius:50%;box-shadow:0 2px 4px rgba(0,0,0,.2)}
.slider-dots{left:578px;top:566px;display:flex;gap:6px}
.slider-dots span{width:9px;height:9px;transform:rotate(45deg);background:var(--ink)}
.slider-dots span:first-child{background:var(--orange)}

/* headings */
.eyebrow{font-size:17px;letter-spacing:5px;color:var(--ink);font-weight:400}
.sec-title{font-size:30px;font-weight:500;line-height:1.15;color:var(--ink)}
.sec-title b{color:var(--orange);font-weight:500}

/* company */
.company-photo{position:absolute;border-radius:50%}
.company-text{left:622px;top:680px;width:460px}
.company-sub{font-size:13px;color:var(--orange);margin-top:6px}
.company-body{font-size:11.5px;line-height:18.6px;color:var(--muted);margin-top:14px}

/* services */
.service-intro{left:94px;top:1132px;width:160px}
.service-intro p{font-size:11px;line-height:17px;color:var(--muted);margin-top:10px}
.arrow-btn{width:35px;height:35px;border-radius:50%;display:flex;align-items:center;justify-content:center}
.service-card{position:absolute;top:1080px;width:205px;height:318px;background:linear-gradient(180deg,var(--orange-soft),#ff4d12);color:var(--white);padding:0 15px}
.service-icon{width:70px;height:70px;border-radius:50%;border:2px solid rgba(255,255,255,.8);margin:26px auto 0 52px;display:flex;align-items:center;justify-content:center}
.service-card h3{font-size:15px;font-weight:400;line-height:19px;margin-top:20px}
.service-card p{font-size:11px;line-height:18.6px;margin-top:6px;color:#ffe6dc}
.service-card a{display:block;font-size:11.5px;font-weight:500;color:var(--white);margin-top:9px}
.service-photo{position:absolute;top:1080px;width:205px;height:369px}

/* blog */
.blog-band{left:0;top:1511px;width:1200px;height:728px;background:var(--grey-bg)}
.center-head{left:0;width:1200px;text-align:center}
.blog-sub{font-size:13px;line-height:20px;color:var(--ink);margin-top:8px}
.post{position:absolute;top:1700px;width:322px}
.post-photo{height:243px}
.post-date{font-size:13px;color:var(--orange);margin-top:12px}
.post h3{font-size:19px;font-weight:500;line-height:24px;margin-top:6px;color:var(--ink)}
.post p{font-size:11.5px;line-height:18px;color:var(--muted);margin-top:8px}

/* team */
.member{position:absolute;background:linear-gradient(180deg,#d6d6d6,#a8a8a8)}
.member-caption{position:absolute;left:0;bottom:18px;width:100%;text-align:center;color:var(--white)}
.team-head{left:780px;top:2296px;width:285px;text-align:right}
.team-head p{font-size:11.5px;line-height:18px;color:var(--muted);margin-top:8px}

/* newsletter */
.newsletter{left:0;top:2997px;width:1200px;height:253px;background:var(--sky)}
.signup{left:319px;top:3141px;width:561px;height:38px;background:var(--white);border-radius:20px;box-shadow:0 3px 6px rgba(0,0,0,.15);display:flex;align-items:center;padding-left:28px;font-size:12px;color:var(--muted)}
.signup-btn{position:absolute;right:8px;top:4px;width:108px;height:30px;border-radius:15px;background:var(--orange);color:var(--white);font-size:13px;font-weight:700;display:flex;align-items:center;justify-content:center}

/* partners */
.partners{left:0;top:3250px;width:794px;height:94px;background:var(--black)}
.partner{position:absolute;top:18px;width:90px;text-align:center;color:var(--white)}
.partner i{display:block;width:40px;height:40px;border:2px solid var(--white);border-radius:50%;margin:0 auto 6px}
.partner span{font-size:9px;letter-spacing:3px}
.callout{left:794px;top:3250px;width:406px;height:94px;background:var(--orange);color:var(--white);padding:26px 0 0 50px}
.callout small{font-size:11px;display:block}
.callout strong{font-size:17px;font-weight:500;display:block;margin-top:6px}

/* footer */
.footer{left:0;top:3344px;width:1200px;height:389px;background:var(--footer);color:#cfcfcf}
.foot-col{position:absolute;top:56px}
.foot-col h4{font-size:15px;font-weight:400;color:#e5e5e5;margin-bottom:14px}
.foot-col li{list-style:none;font-size:11.5px;line-height:29px;white-space:nowrap}
.foot-col li::before{content:"→";color:var(--orange);margin-right:5px;font-size:10px}
.contact-row{display:flex;align-items:flex-start;gap:12px;font-size:11.5px;line-height:17px;margin-bottom:18px}
.contact-ico{width:20px;height:20px;border:1px solid var(--orange);display:flex;align-items:center;justify-content:center;flex-shrink:0}
.social-row{display:flex;align-items:center;gap:10px;font-size:12px;margin-bottom:16px}
.social-row i{width:26px;height:26px;border-radius:50%;border:2px solid var(--white);background:#3b5998;display:block}
.foot-brand{left:0;width:1200px;top:232px;text-align:center;color:var(--white)}
.foot-brand .dot{width:22px;height:22px;border-radius:50%;background:var(--orange);margin:0 auto 8px}
.foot-brand .name{font-size:16px;font-weight:700;letter-spacing:.3px}
.foot-brand .tag{font-size:10px}
.copyright{left:0;width:1200px;top:321px;text-align:center;font-size:11.5px;color:#cfcfcf}
</style>
</head>
<body>

<!-- Header -->
<header>
  <div class="abs brand">
    <div class="brand-dot"></div>
    <div class="brand-name">BRIGHTPATH DIGITAL</div>
    <div class="brand-tag">Online Marketing. Elevated</div>
  </div>
  <nav class="abs nav">
    <a class="active" style="left:0">HOME</a>
    <a style="left:66px">INTERIOR</a>
    <a style="left:171px">BLOG</a>
    <a style="left:253px">CONTACT US</a>
  </nav>
</header>

<!-- Hero -->
<section class="hero">
  <svg class="abs" style="left:638px;top:0" width="562" height="600" viewBox="0 0 562 600" role="img" aria-label="Photo of a team of four colleagues discussing charts around a desk by a window">
    <defs>
      <linearGradient id="heroTone" x1="0" y1="0" x2="1" y2="1">
        <stop offset="0" stop-color="#f8cdb9"/>
        <stop offset=".55" stop-color="#e9a98f"/>
        <stop offset="1" stop-color="#d9cfcb"/>
      </linearGradient>
    </defs>
    <path d="M72 0 L562 0 L562 545 C520 578 420 600 330 585 C230 570 170 520 120 470 C70 420 22 380 32 300 C42 230 12 190 32 140 C47 90 82 60 72 0 Z" fill="url(#heroTone)"/>
  </svg>
  <svg class="abs" style="left:636px;top:138px" width="40" height="40"><polygon points="16,0 36,32 0,36" fill="var(--orange)"/></svg>
  <svg class="abs" style="left:640px;top:302px" width="14" height="14"><polygon points="13,0 13,14 0,7" fill="var(--orange)"/></svg>
  <div class="abs" style="left:817px;top:517px;width:57px;height:53px;background:#333"></div>
  <div class="abs social-dot" style="left:983px;top:553px;background:#1f5fd6"></div>
  <div class="abs social-dot" style="left:1030px;top:553px;background:#3ab0e8;border:3px solid #fff"></div>
  <div class="abs social-dot" style="left:1075px;top:553px;background:#e54878;border:3px solid #fff"></div>

  <h1 class="abs hero-title">
    <div class="l1">ONLINE</div>
    <div class="l2">MARKETING</div>
    <div class="l3">AGENCY</div>
  </h1>
  <p class="abs hero-lead">It is a long established fact that a reader will be distracted by the readable content of a page ...</p>
  <a class="btn" style="left:94px;top:410px;width:113px;height:32px">RED MORE</a>
  <div class="abs hero-call"><span class="orange">Caall Us:</span><br>+1 (555) 014 2290</div>
  <div class="abs slider-dots"><span></span><span></span><span></span></div>
</section>

<!-- Company information -->
<section class="company">
  <svg class="abs" style="left:90px;top:640px" width="400" height="380">
    <circle cx="110" cy="113" r="103" fill="none" stroke="var(--orange)" stroke-width="3"/>
    <circle cx="301" cy="106" r="71" fill="none" stroke="#ddd" stroke-width="3"/>
  </svg>
  <div class="company-photo" role="img" aria-label="Photo of a smiling businessman working on a laptop" style="left:174px;top:670px;width:196px;height:196px;background:linear-gradient(160deg,#d7a16b,#7b7f86)"></div>
  <div class="company-photo" role="img" aria-label="Photo of marketing brochures and printed material" style="left:365px;top:793px;width:110px;height:110px;background:linear-gradient(160deg,#f1f1f1,#9a9a9a)"></div>
  <div class="company-photo" role="img" aria-label="Photo of a desktop computer on an office desk" style="left:101px;top:847px;width:160px;height:160px;background:linear-gradient(160deg,#e9e9e9,#6f6f72)"></div>
  <div class="company-photo" role="img" aria-label="Photo of hands working on a laptop with documents" style="left:269px;top:868px;width:134px;height:134px;background:linear-gradient(160deg,#e3e9ef,#788190)"></div>

  <div class="abs" style="left:589px;top:652px;width:1px;height:355px;background:#ddd"></div>
  <div class="abs" style="left:588px;top:652px;width:3px;height:54px;background:var(--orange)"></div>

  <div class="abs company-text">
    <div class="eyebrow">OUR</div>
    <h2 class="sec-title"><b>C</b>OMPANY<br>INFORMATION</h2>
    <div class="company-sub">That Specializes In Search Marketing (SEM)</div>
    <p class="company-body">It is a long established fact that a reader will be distracted by the readable content of a page when looking at its layout. The point of using Lorem Ipsum is that it has a more-or-less normal distribution of letters, as opposed to using 'Content here, content here', making it look like readable English. Many desktop publishing packages and web page editors now use Lorem Ipsum as their default model text, and a search for 'lorem ipsum' will uncover many web sites still in their infancy. Various versions have evolved over the years, sometimes by accident, sometimes ....</p>
  </div>
  <a class="btn" style="left:617px;top:953px;width:112px;height:32px">RED MORE</a>
</section>

<!-- Marketing services -->
<section class="services">
  <div class="abs service-intro">
    <div class="eyebrow">OUR</div>
    <h2 class="sec-title"><b>M</b>arketing<br>Service</h2>
    <p>There are many variations of passages of Lorem Ipsum available, but the majority have suffered alteration in some form, by injected humour,</p>
  </div>
  <div class="abs arrow-btn" style="left:94px;top:1359px;border:1.5px solid var(--ink)">
    <svg width="16" height="12" viewBox="0 0 16 12"><path d="M15 6H2M6 1L1 6l5 5" fill="none" stroke="var(--ink)" stroke-width="2"/></svg>
  </div>
  <div class="abs arrow-btn" style="left:139px;top:1359px;border:1.5px solid var(--orange)">
    <svg width="16" height="12" viewBox="0 0 16 12"><path d="M1 6h13M10 1l5 5-5 5" fill="none" stroke="var(--orange)" stroke-width="2"/></svg>
  </div>

  <article class="service-card" style="left:285px">
    <div class="service-icon"><svg width="30" height="30" viewBox="0 0 30 30"><circle cx="15" cy="8" r="4" fill="#fff"/><path d="M9 26v-8a6 6 0 0 1 12 0v8" fill="#fff"/><circle cx="4" cy="20" r="2" fill="#fff"/><circle cx="26" cy="20" r="2" fill="#fff"/></svg></div>
    <h3>Business Marketing<br>Strategy</h3>
    <p>Let us strategize the big picture for you. With decades of experience, we have seen what works and what doesn't. And we can leverage all that experience for your business.</p>
    <a>READ MORE</a>
  </article>
  <div class="service-photo" role="img" aria-label="Photo of hands reviewing printed charts and graphs on a table" style="left:490px;background:linear-gradient(160deg,#eceae6,#b9b6b0)"></div>
  <article class="service-card" style="left:695px">
    <div class="service-icon"><svg width="28" height="30" viewBox="0 0 28 30"><rect x="4" y="3" width="20" height="24" rx="2" fill="none" stroke="#fff" stroke-width="2"/><path d="M8 10h12M8 15h12M8 20h8" stroke="#fff" stroke-width="2"/></svg></div>
    <h3>Content Creation<br>and Marketing</h3>
    <p>You've heard it before. "Content is king." Search engines love it and potential customers expect it. Our content creators have years of experience working with Top 500, 100 and 50</p>
    <a>READ MORE</a>
  </article>
  <div class="service-photo" role="img" aria-label="Photo of a notebook page with an online marketing sketch" style="left:900px;background:linear-gradient(160deg,#e6e3dc,#c7c2b8)"></div>
</section>

<!-- Blog -->
<section class="blog">
  <div class="abs blog-band"></div>
  <div class="abs center-head" style="top:1569px">
    <div class="eyebrow">OUR</div>
    <h2 class="sec-title"><b>B</b>LOG POST</h2>
    <p class="blog-sub">The standard chunk of Lorem Ipsum used since the 1500s is reproduced<br>below for those interested.</p>
  </div>
  <article class="post" style="left:94px">
    <div class="post-photo" role="img" aria-label="Illustration of web design and marketing doodles on a chalkboard" style="background:linear-gradient(160deg,#dcdcdc,#9c9c9c)"></div>
    <div class="post-date">July 06, 2019</div>
    <h3>Business Mistakes to Avoid When Starting a Business</h3>
    <p>There are many variations of passages of Lorem Ipsum available, but the majority have suffered alteration in some form, by injected humour, or randomised words which don't look even .</p>
  </article>
  <article class="post" style="left:439px">
    <div class="post-photo" role="img" aria-label="Photo of a presenter leading a business meeting" style="background:linear-gradient(160deg,#e8e6e2,#8d8a86)"></div>
    <div class="post-date">July 06, 2019</div>
    <h3>Business Mistakes to Avoid When Starting a Business</h3>
    <p>There are many variations of passages of Lorem Ipsum available, but the majority have suffered alteration in some form, by injected humour, or randomised words which don't look even .</p>
  </article>
  <article class="post" style="left:784px">
    <div class="post-photo" role="img" aria-label="Photo of SEO tools and keyword labels laid on a dark surface" style="background:linear-gradient(160deg,#6d6258,#2f2c2a)"></div>
    <div class="post-date">July 06, 2019</div>
    <h3>Business Mistakes to Avoid When Starting a Business</h3>
    <p>There are many variations of passages of Lorem Ipsum available, but the majority have suffered alteration in some form, by injected humour, or randomised words which don't look even .</p>
  </article>
  <a class="btn" style="left:523px;top:2142px;width:152px;height:33px">VIEW ALL BLOG</a>
</section>

<!-- Team -->
<section class="team">
  <div class="member" role="img" aria-label="Portrait of a team member in a white shirt" style="left:94px;top:2394px;width:246px;height:236px"></div>
  <div class="member" role="img" aria-label="Portrait of a team member in a dark t-shirt" style="left:349px;top:2304px;width:246px;height:235px"></div>
  <div class="member" role="img" aria-label="Portrait of the company CEO" style="left:349px;top:2550px;width:246px;height:235px;background:linear-gradient(180deg,#d0d0d0,#6a6a6a 70%,#2b2b2b)">
    <div class="member-caption"><div style="font-size:16px;font-weight:500">LOREM IPSUM</div><div style="font-size:11px;letter-spacing:2px;margin-top:4px">CEO</div></div>
  </div>
  <div class="member" role="img" aria-label="Portrait of a team member in a suit" style="left:604px;top:2453px;width:248px;height:236px"></div>
  <div class="member" role="img" aria-label="Portrait of a senior team member wearing glasses" style="left:604px;top:2699px;width:248px;height:235px"></div>
  <div class="member" role="img" aria-label="Portrait of a team member in a dark blazer" style="left:861px;top:2545px;width:246px;height:236px"></div>
  <div class="abs team-head">
    <div class="eyebrow">MEET</div>
    <h2 class="sec-title"><b>O</b>UR TEAM</h2>
    <p>There are many variations of passages of Lorem Ipsum available, but the majority have suffered alteration in some form</p>
  </div>
</section>

<!-- Newsletter -->
<section class="newsletter-block">
  <div class="abs newsletter"></div>
  <div class="abs center-head" style="top:3055px">
    <div class="eyebrow">SIGN UP</div>
    <h2 class="sec-title"><b>N</b>EWSLETTER</h2>
  </div>
  <div class="abs signup">
    <svg width="16" height="11" viewBox="0 0 16 11" style="margin-right:8px"><rect x="0.5" y="0.5" width="15" height="10" fill="none" stroke="#777"/><path d="M1 1l7 5 7-5" fill="none" stroke="#777"/></svg>
    Enter Your Email Address:
    <span class="signup-btn">SUBSCRIB</span>
  </div>
</section>

<!-- Partners & call -->
<section>
  <div class="abs partners">
    <div class="partner" style="left:115px"><i></i><span>COMPANY</span></div>
    <div class="partner" style="left:251px"><i></i><span>COMPANY</span></div>
    <div class="partner" style="left:387px"><i></i><span>COMPANY</span></div>
    <div class="partner" style="left:540px"><i></i><span>COMPANY</span></div>
    <div class="partner" style="left:684px"><i></i><span>COMPANY</span></div>
  </div>
  <div class="abs callout">
    <small>Do You Have Any Question?</small>
    <strong>Call Us: +1 (555) 014 2290</strong>
  </div>
</section>

<!-- Footer -->
<footer class="abs footer">
  <div class="foot-col" style="left:106px">
    <h4>Sitemap</h4>
    <ul><li>Home</li><li>Interior</li><li>Blog</li><li>Contact Us</li></ul>
  </div>
  <div class="foot-col" style="left:271px">
    <h4>Services</h4>
    <ul><li>Content Creation and Marketing</li><li>Graphic &amp; Publication Design</li><li>Pay Per Click (PPC) Management</li><li>Search Engine Optimization</li></ul>
  </div>
  <div class="foot-col" style="left:484px;top:85px">
    <ul><li>Social Media Management</li><li>Video Production &amp; Editing</li><li>Website Hosting &amp; Management</li><li>Website Design &amp; Development</li></ul>
  </div>
  <div class="foot-col" style="left:768px">
    <h4>Contact Us</h4>
    <div class="contact-row"><span class="contact-ico"><svg width="10" height="12" viewBox="0 0 10 12"><path d="M5 11S1 6.5 1 4a4 4 0 0 1 8 0c0 2.5-4 7-4 7z" fill="var(--orange)"/><circle cx="5" cy="4" r="1.5" fill="var(--footer)"/></svg></span><span>Lorem Ipsum<br>48 Harbor Lane, Springfield</span></div>
    <div class="contact-row"><span class="contact-ico"><svg width="11" height="11" viewBox="0 0 11 11"><path d="M2 1l2 2-1 1.5a6 6 0 0 0 3.5 3.5L8 7l2 2-1.5 1.5C5 10 1 6 .5 2.5z" fill="var(--orange)"/></svg></span><span>+1 (555) 014 2290</span></div>
    <div class="contact-row"><span class="contact-ico"><svg width="12" height="9" viewBox="0 0 12 9"><rect x="0.5" y="0.5" width="11" height="8" fill="var(--orange)"/><path d="M1 1l5 4 5-4" fill="none" stroke="var(--footer)"/></svg></span><span>hello@brightpathmail.com</span></div>
  </div>
  <div class="foot-col" style="left:1001px">
    <h4>Social Media</h4>
    <div class="social-row"><i></i>Pagefeed</div>
    <div class="social-row"><i style="background:#2a9de0"></i>Shortposts</div>
    <div class="social-row"><i style="background:#e0457b"></i>Photostream</div>
  </div>
  <div class="abs foot-brand">
    <div class="dot"></div>
    <div class="name">BRIGHTPATH DIGITAL</div>
    <div class="tag">Online Marketing. Elevated</div>
  </div>
  <div class="abs copyright">© 2020, <span class="orange">Brightpath Digital</span>. All Rights Reserved.</div>
</footer>

</body>
</html>
```